Business card design needed

We are a unique and exciting Drama, Dance and Fitness studio that offers classes from 18 months to adults - with a strong focus on the Under 5's market and we mainly cater for children under 14 years. We aim to create confidence in ALL of our students. We have a very happy and encouraging environment at our studio so would like my business card to 'project this'. I would like my 'catchphrase' - "Building Belief" - Step up and GLOW! to be on the front of my business card also.

Myself as the Principal has a VERY bubbly personality - so I need this business card to project this also. Stars(silver?) and perhaps pictures/silouettes of happy children would be appropriate. And as we also have adult fitness classes, pictures/silouettes of adults in yoga poses/exercise poses would be nice to have too. We are a very 'theatrical' school so would like my business card to look as 'exciting' as possible - but incorporating my school colours of red, royal blue, silver and white.
Updates

                                       

Hi everyone - thankyou so far for your designs.  I feel like I need to show a bit more 'excitement' with the business cards that I have seen so far.  I would definitely like to see stars(preferably silver) on there, and preferably pictures/silhouettes of children happy/performing.  If you can fit pictures/silouettes of adults exercising - yoga/zumba etc that would be a bonus.  I have got an extremely bubbly, theatrical personality, so I need that to be reflected with my name and title on the card also. The colour scheme of my colours red, royal blue, silver and white is a priority too and most of you have done this.  Thankyou.                                   

Target Market(s)

Families with children - especially those who love to perform, and for adults who like to exercise.

Industry/Entity Type

Environment

Contact Information for Business Card

Delphine's Limelighters - Stage Movement Theatre and Wellness Studio. Unit 4, 58 Brellington Rd MARLOWE HEIGHTS. "Building Belief" - Step up and GLOW! Delphine Kowalczyk PRINCIPAL. Phone: 0499 562184 Email: brightkid@qvrnet.com.au Web: www.delphineslimelighters.com.au

Requirements
Must have
• Our studio colours are Red, Royal Blue with a bit of silver and white. I also LOVE stars - and this would suit my business card. Also need to have my logo on there - which I have uploaded. I would like my 'catchphrase' - "Building Belief" - Step up and GLOW! to be on the front of my business card also.
Nice to have
• Pictures/silouettes of happy children would be appropriate. And as we also have adult fitness classes, pictures/silouettes of adults in yoga poses/exercise poses would be nice to have too. We are a very 'theatrical' school so would like my business card to look as 'exciting' as possible - but incorporating my school colours of red, royal blue, silver and white.

```html
<!DOCTYPE html>
<html lang="en">
<head>
<meta charset="utf-8">
<title>Delphine's Limelighters Business Card</title>
<link rel="stylesheet" href="https://fonts.googleapis.com/css2?family=Lobster&family=Ubuntu:wght@500;700&family=Quicksand:wght@500&display=swap">
<style>
  :root {
    --stage: #e4e5e7;
    --card-white: #ffffff;
    --card-silver: #dcdde0;
    --royal-blue: #2a3f9e;
    --blue-line: #3350b8;
    --red: #c8161d;
    --red-deep: #9c0f16;
    --red-light: #d8242b;
    --quote-red: #c41820;
    --silver-light: #fbfbfc;
    --silver-mid: #b9bcc2;
    --silver-dark: #7d8189;
    --white: #ffffff;
  }
  * { box-sizing: border-box; margin: 0; padding: 0; }
  html, body { width: 1200px; height: 861px; overflow: hidden; }
  body { background: var(--stage); position: relative; }

  .business-card {
    position: absolute;
    left: 150px; top: 170px;
    width: 900px; height: 520px;
    border-radius: 4px;
    overflow: hidden;
    box-shadow: 0 14px 40px rgba(0,0,0,.25);
    background: var(--card-white);
  }

  .card-header {
    position: absolute; left: 0; top: 0;
    width: 100%; height: 190px;
    background: linear-gradient(180deg, var(--card-white) 0%, var(--card-white) 45%, var(--card-silver) 100%);
  }
  .brand {
    position: absolute; left: 50px; top: 50px; width: 520px;
    text-align: center;
  }
  .brand-name {
    display: flex; align-items: center; justify-content: center; gap: 12px;
    font-family: "Ubuntu", sans-serif; font-weight: 700;
    font-size: 42px; color: var(--royal-blue); line-height: 1.1;
    white-space: nowrap;
  }
  .brand-mark {
    width: 18px; height: 18px; border-radius: 50%;
    background: var(--royal-blue); flex: none;
  }
  .brand-tagline {
    margin-top: 18px;
    font-family: "Ubuntu", sans-serif; font-weight: 700;
    font-size: 18px; color: var(--royal-blue); white-space: nowrap;
  }

  .catchphrase {
    position: absolute; left: 600px; top: 50px; width: 260px;
    text-align: center;
    font-family: "Ubuntu", sans-serif; font-weight: 700;
    color: var(--quote-red); line-height: 1.1;
  }
  .catchphrase-line { font-size: 30px; white-space: nowrap; }
  .catchphrase-sub {
    margin-top: 4px;
    font-size: 14px; font-weight: 500; white-space: nowrap;
  }

  .divider {
    position: absolute; left: 0; top: 190px;
    width: 100%; height: 10px; background: var(--blue-line);
  }

  .card-body {
    position: absolute; left: 0; top: 200px;
    width: 100%; height: 320px;
    background: radial-gradient(ellipse at 50% 30%, var(--red-light) 0%, var(--red) 50%, var(--red-deep) 100%);
  }

  .person-name {
    position: absolute; left: 0; top: 18px; width: 100%;
    text-align: center;
    font-family: "Lobster", cursive; font-size: 64px; line-height: 1;
    letter-spacing: 1px;
    background: linear-gradient(180deg, var(--silver-light) 0%, var(--silver-mid) 48%, var(--silver-dark) 52%, var(--silver-light) 100%);
    -webkit-background-clip: text; background-clip: text; color: transparent;
    filter: drop-shadow(0 3px 2px rgba(60,0,0,.55));
  }
  .person-title {
    position: absolute; left: 0; top: 92px; width: 100%;
    text-align: center;
    font-family: "Lobster", cursive; font-size: 30px; color: var(--white);
  }

  .contact-list {
    position: absolute; left: 0; top: 148px; width: 100%;
    font-family: "Quicksand", sans-serif; font-weight: 500;
    font-size: 22px; color: var(--white);
  }
  .contact-row {
    display: flex; justify-content: center; gap: 48px;
    margin-bottom: 14px;
  }
  .contact-item { display: flex; align-items: center; gap: 8px; white-space: nowrap; }
  .contact-icon { width: 24px; height: 24px; flex: none; }
</style>
</head>
<body>
  <div class="business-card">
    <header class="card-header">
      <div class="brand">
        <div class="brand-name"><span class="brand-mark"></span>Delphine's Limelighters</div>
        <div class="brand-tagline">Stage Movement Theatre and Wellness Studio</div>
      </div>
      <div class="catchphrase">
        <div class="catchphrase-line">"Building</div>
        <div class="catchphrase-line">Belief"</div>
        <div class="catchphrase-sub">- Step up and GLOW!</div>
      </div>
    </header>

    <div class="divider"></div>

    <section class="card-body">
      <div class="person-name">Delphine Kowalczyk</div>
      <div class="person-title">Principal</div>

      <div class="contact-list">
        <div class="contact-row">
          <span class="contact-item">
            <svg class="contact-icon" viewBox="0 0 24 24" aria-hidden="true">
              <circle cx="12" cy="12" r="11" fill="#fff"/>
              <rect x="7" y="6" width="10" height="12" fill="#c8161d"/>
              <rect x="9" y="8" width="2" height="2" fill="#fff"/><rect x="13" y="8" width="2" height="2" fill="#fff"/>
              <rect x="9" y="12" width="2" height="2" fill="#fff"/><rect x="13" y="12" width="2" height="2" fill="#fff"/>
            </svg>
            Studio. Unit 4, 58 Brellington Rd, MARLOWE HEIGHTS
          </span>
        </div>
        <div class="contact-row">
          <span class="contact-item">
            <svg class="contact-icon" viewBox="0 0 24 24" aria-hidden="true">
              <circle cx="12" cy="12" r="11" fill="#fff"/>
              <path d="M8 17 L16 7" stroke="#c8161d" stroke-width="3" stroke-linecap="round"/>
            </svg>
            0499 562184
          </span>
          <span class="contact-item">
            <svg class="contact-icon" viewBox="0 0 24 24" aria-hidden="true">
              <circle cx="12" cy="12" r="11" fill="#fff"/>
              <rect x="6" y="8" width="12" height="8" fill="#c8161d"/>
              <path d="M6 8 L12 13 L18 8" stroke="#fff" stroke-width="1.4" fill="none"/>
            </svg>
            brightkid@qvrnet.com.au
          </span>
        </div>
        <div class="contact-row">
          <span class="contact-item">
            <svg class="contact-icon" viewBox="0 0 24 24" aria-hidden="true">
              <circle cx="12" cy="12" r="11" fill="#fff"/>
              <rect x="6" y="7" width="12" height="8" rx="1" fill="#c8161d"/>
              <rect x="9" y="16" width="6" height="1.6" fill="#c8161d"/>
            </svg>
            www.delphineslimelighters.com.au
          </span>
        </div>
      </div>
    </section>
  </div>
</body>
</html>
```